VELTO video wall installation examples

To provide a PDF brochure to professionally present to prospective customers (schools) of our previous installation projects for the VELTO brand of video wall displays. (example draft) Only these photos and text is to be included in this new brochure - Each photo is relative to an individual site location (school) , with specifications and cost of the installation. I would suggest having two site locations per page, with the VELTO logo, page border and clear heading for the site location on each page. I have attached a sample in WORD format of the intended look and copy but needs to be made a lot more attractive for presentation. The file (velto brochure A4) is provided as a guide only to a previous brochure showing the colours and designs for information only.

```html
<!DOCTYPE html>
<html lang="en">
<head>
<meta charset="utf-8">
<title>VELTO – Installation Examples</title>
<link rel="stylesheet" href="https://fonts.googleapis.com/css2?family=Montserrat:wght@700;800;900&family=Open+Sans:wght@400;600&display=swap">
<style>
  :root {
    --red: #e3202a;
    --ink: #2a2a2a;
    --footer: #2c2c2c;
    --spec-bg: #ececec;
    --paper: #ffffff;
    --backdrop: #a6a6a6;
    --muted: #555555;
  }
  * { box-sizing: border-box; margin: 0; padding: 0; }
  html, body { width: 1200px; height: 4307px; overflow: hidden; }
  body {
    background: var(--backdrop);
    font-family: "Open Sans", Arial, sans-serif;
    color: var(--ink);
  }
  .sheet {
    display: grid;
    grid-template-columns: 540px 540px;
    grid-auto-rows: 765px;
    column-gap: 40px;
    row-gap: 80px;
    padding: 80px 40px 0;
  }
  .brochure-page {
    background: var(--paper);
    position: relative;
    display: flex;
    flex-direction: column;
    box-shadow: 0 4px 14px rgba(0,0,0,.28);
    overflow: hidden;
  }
  .cover { grid-column: 1 / span 2; justify-self: center; width: 540px; }

  /* Wordmark */
  .wordmark {
    display: flex; align-items: center; justify-content: center; gap: 10px;
  }
  .wordmark-name {
    font-family: "Montserrat", Arial, sans-serif;
    font-weight: 900;
    color: var(--ink);
    letter-spacing: 2px;
    line-height: 1;
  }
  .wordmark-dot { background: var(--red); }

  /* Cover */
  .cover-head { height: 150px; display: flex; align-items: center; justify-content: center; }
  .cover-head .wordmark-name { font-size: 64px; }
  .cover-head .wordmark-dot { width: 18px; height: 18px; }
  .cover-rule { height: 8px; background: var(--ink); }
  .cover-collage { display: block; width: 540px; height: 440px; }
  .cover-title {
    flex: 1;
    display: flex; flex-direction: column; align-items: center; justify-content: center;
    font-family: "Montserrat", Arial, sans-serif; font-weight: 800;
    font-size: 58px; line-height: 1;
  }
  .cover-title .line-dark { color: var(--ink); }
  .cover-title .line-red { color: var(--red); margin-top: 2px; }
  .cover-contact {
    height: 30px; background: var(--footer); color: #fff;
    font-size: 15px; letter-spacing: .5px;
    display: flex; align-items: center; justify-content: center;
  }

  /* Project pages */
  .page-head { height: 84px; display: flex; align-items: center; justify-content: center; padding-top: 6px; }
  .page-head .wordmark-name { font-size: 40px; }
  .page-head .wordmark-dot { width: 12px; height: 12px; }
  .site-title {
    height: 34px; background: var(--red); color: #fff;
    font-weight: 600; font-size: 22px; letter-spacing: .4px;
    display: flex; align-items: center; justify-content: center;
    text-transform: uppercase;
  }
  .spec-box {
    align-self: center;
    width: 200px; min-height: 178px;
    margin: 0 0 18px;
    background: var(--spec-bg);
    display: flex; flex-direction: column; justify-content: center;
    padding: 10px 8px;
    list-style: none;
  }
  .spec-box.wide { width: 230px; }
  .spec-box li {
    font-size: 12px; line-height: 27px; color: var(--muted);
    text-align: center;
  }
  .spec-box.dense li { line-height: 21px; }
  .spec-box li::before {
    content: ""; display: inline-block;
    width: 7px; height: 7px; margin-right: 8px;
    border: 2px solid var(--red); border-radius: 50%;
    vertical-align: 0;
  }
  .spec-box li.note::before { display: none; }
  .spec-box li.note { line-height: 15px; margin-top: 4px; }

  .page-media {
    flex: 1; position: relative;
    padding: 0 32px 12px;
    display: flex;
  }
  .page-media::after {
    content: ""; position: absolute; left: 0; right: 0; bottom: 0;
    height: 30px; background: var(--red);
  }
  .page-media::before {
    content: ""; position: absolute; right: 22px; top: 0;
    width: 3px; height: 55%; background: var(--red);
  }
  .site-photo {
    position: relative; z-index: 1; flex: 1;
    border: 3px solid var(--red);
  }
  .photo-hall { background: linear-gradient(180deg, #5d5f63 0%, #b9a98a 45%, #a7703f 100%); }
  .photo-court { background: linear-gradient(180deg, #6f757d 0%, #9aa0a6 50%, #8a5a32 100%); }
  .photo-outdoor { background: linear-gradient(180deg, #6b7688 0%, #50575f 55%, #7f9a56 100%); }
  .photo-facade { background: linear-gradient(160deg, #4a5560 0%, #263444 50%, #7d7f82 100%); }
  .photo-street { background: linear-gradient(180deg, #aac2d6 0%, #5f7a4a 50%, #8c8c8c 100%); }

  .page-footer {
    height: 64px; background: var(--footer); color: #e8e8e8;
    display: flex; align-items: center; padding: 0 30px;
    font-size: 11px; letter-spacing: .6px;
  }
  .page-footer .bullet {
    width: 11px; height: 11px; border: 2px solid #cfcfcf; border-radius: 50%;
    margin-right: 8px;
  }
  .page-footer .sep { margin: 0 10px; }
  .page-number {
    margin-left: auto;
    width: 20px; height: 20px; border-radius: 50%; background: #fff;
    color: var(--red); font-weight: 600; font-size: 11px;
    display: flex; align-items: center; justify-content: center;
  }
</style>
</head>
<body>
<main class="sheet">

  <section class="brochure-page cover">
    <header class="cover-head">
      <div class="wordmark"><span class="wordmark-name">VELTO</span><span class="wordmark-dot"></span></div>
    </header>
    <div class="cover-rule"></div>
    <svg class="cover-collage" viewBox="0 0 540 440" role="img" aria-label="Four installation photos: indoor gym video walls, an outdoor facade screen and a school entrance sign">
      <defs>
        <linearGradient id="gymA" x1="0" y1="0" x2="0" y2="1"><stop offset="0" stop-color="#5c5f66"/><stop offset=".55" stop-color="#a9a9a6"/><stop offset="1" stop-color="#b07c48"/></linearGradient>
        <linearGradient id="gymB" x1="0" y1="0" x2="0" y2="1"><stop offset="0" stop-color="#70757c"/><stop offset=".6" stop-color="#9a9ea3"/><stop offset="1" stop-color="#7e5630"/></linearGradient>
        <linearGradient id="outA" x1="0" y1="0" x2="0" y2="1"><stop offset="0" stop-color="#7b8692"/><stop offset=".6" stop-color="#4b525a"/><stop offset="1" stop-color="#7f8a70"/></linearGradient>
        <linearGradient id="outB" x1="0" y1="0" x2="0" y2="1"><stop offset="0" stop-color="#b7cadb"/><stop offset=".5" stop-color="#5c7a48"/><stop offset="1" stop-color="#8a8a8a"/></linearGradient>
      </defs>
      <polygon points="0,0 322,0 282,196 0,196" fill="url(#gymA)"/>
      <polygon points="330,0 540,0 540,196 290,196" fill="url(#gymB)"/>
      <polygon points="0,176 286,176 282,196 0,196" fill="#e3202a"/>
      <rect x="0" y="196" width="540" height="14" fill="#e3202a"/>
      <polygon points="0,210 270,210 230,440 0,440" fill="url(#outA)"/>
      <polygon points="278,210 540,210 540,440 238,440" fill="url(#outB)"/>
      <polygon points="0,416 234,416 230,440 0,440" fill="#e3202a"/>
    </svg>
    <h1 class="cover-title"><span class="line-dark">INSTALLATION</span><span class="line-red">EXAMPLES</span></h1>
    <footer class="cover-contact">Call Us Now: (123) 456-7890 &nbsp;|&nbsp; Email: info@veltomail.com</footer>
  </section>

  <section class="brochure-page">
    <header class="page-head"><div class="wordmark"><span class="wordmark-name">VELTO</span><span class="wordmark-dot"></span></div></header>
    <h2 class="site-title">Ashford Vale Primary School</h2>
    <ul class="spec-box">
      <li>P3, 5376 x 3072mm VELTO</li>
      <li>Equipment Rack</li>
      <li>2x powered array speakers</li>
      <li>2x Wireless Mics</li>
      <li>8 channel mixer</li>
      <li>$58,154.35+GST</li>
    </ul>
    <div class="page-media"><div class="site-photo photo-hall" role="img" aria-label="Video wall mounted on a timber-clad hall wall"></div></div>
    <footer class="page-footer"><span class="bullet"></span>Address Goes Here<span class="sep">|</span><span class="bullet"></span>www.webaddress.com<span class="page-number">1</span></footer>
  </section>

  <section class="brochure-page">
    <header class="page-head"><div class="wordmark"><span class="wordmark-name">VELTO</span><span class="wordmark-dot"></span></div></header>
    <h2 class="site-title">Kestrel Ridge Primary School</h2>
    <ul class="spec-box">
      <li>P3, 5376 x 3072mm VELTO</li>
      <li>HDMI extender kit</li>
      <li>Tablet control</li>
      <li>HDMI switcher</li>
      <li>Wireless streaming</li>
      <li>$63,000+GST</li>
    </ul>
    <div class="page-media"><div class="site-photo photo-court" role="img" aria-label="Scoreboard video wall above a basketball court"></div></div>
    <footer class="page-footer"><span class="bullet"></span>Address Goes Here<span class="sep">|</span><span class="bullet"></span>www.webaddress.com<span class="page-number">2</span></footer>
  </section>

  <section class="brochure-page">
    <header class="page-head"><div class="wordmark"><span class="wordmark-name">VELTO</span><span class="wordmark-dot"></span></div></header>
    <h2 class="site-title">Willow Bay Primary School</h2>
    <ul class="spec-box">
      <li>P3, 4608 x 2688mm VELTO</li>
      <li>9 channel mixer</li>
      <li>2x wireless mics</li>
      <li>Existing amp / speakers</li>
      <li>$51,401.93</li>
    </ul>
    <div class="page-media"><div class="site-photo photo-hall" role="img" aria-label="Video wall above a stage opening in a school hall"></div></div>
    <footer class="page-footer"><span class="bullet"></span>Address Goes Here<span class="sep">|</span><span class="bullet"></span>www.webaddress.com<span class="page-number">3</span></footer>
  </section>

  <section class="brochure-page">
    <header class="page-head"><div class="wordmark"><span class="wordmark-name">VELTO</span><span class="wordmark-dot"></span></div></header>
    <h2 class="site-title">Harbourview College</h2>
    <ul class="spec-box">
      <li>P10, 3840 x 1920mm VELTO</li>
      <li>Digital signage media player</li>
      <li>$40,570.05+GST</li>
    </ul>
    <div class="page-media"><div class="site-photo photo-outdoor" role="img" aria-label="Outdoor video wall on a building facade above a lawn"></div></div>
    <footer class="page-footer"><span class="bullet"></span>Address Goes Here<span class="sep">|</span><span class="bullet"></span>www.webaddress.com<span class="page-number">4</span></footer>
  </section>

  <section class="brochure-page">
    <header class="page-head"><div class="wordmark"><span class="wordmark-name">VELTO</span><span class="wordmark-dot"></span></div></header>
    <h2 class="site-title">Harbourview College</h2>
    <ul class="spec-box">
      <li>P3, 2688 x 1728mm VELTO</li>
      <li>Digital signage player</li>
      <li>$41,128+GST</li>
    </ul>
    <div class="page-media"><div class="site-photo photo-facade" role="img" aria-label="Video wall set into a dark exterior wall showing notices"></div></div>
    <footer class="page-footer"><span class="bullet"></span>Address Goes Here<span class="sep">|</span><span class="bullet"></span>www.webaddress.com<span class="page-number">5</span></footer>
  </section>

  <section class="brochure-page">
    <header class="page-head"><div class="wordmark"><span class="wordmark-name">VELTO</span><span class="wordmark-dot"></span></div></header>
    <h2 class="site-title">Harbourview College</h2>
    <ul class="spec-box wide dense">
      <li>P3, 4608 x 2304mm VELTO</li>
      <li>9 channel mixer</li>
      <li>HDMI switcher</li>
      <li>Equipment Rack</li>
      <li>Wireless presentation</li>
      <li>HDMI extension kit</li>
      <li>2x wireless mics</li>
      <li>In wall touchscreen controller</li>
      <li>2x Aurel speaker array</li>
      <li>$68,176.64</li>
    </ul>
    <div class="page-media"><div class="site-photo photo-court" role="img" aria-label="Large video wall in a sports hall with timber floor"></div></div>
    <footer class="page-footer"><span class="bullet"></span>Address Goes Here<span class="sep">|</span><span class="bullet"></span>www.webaddress.com<span class="page-number">6</span></footer>
  </section>

  <section class="brochure-page">
    <header class="page-head"><div class="wordmark"><span class="wordmark-name">VELTO</span><span class="wordmark-dot"></span></div></header>
    <h2 class="site-title">Elmstead Secondary College</h2>
    <ul class="spec-box dense">
      <li>P6, 7680 x 4608mm VELTO</li>
      <li>HDMI switcher</li>
      <li>Tablet control</li>
      <li>1x wireless mic</li>
      <li>Aurel amp and speakers</li>
      <li>Streaming audio</li>
      <li>Bluray player</li>
      <li>Rack</li>
      <li>$117,938.03+GST</li>
    </ul>
    <div class="page-media"><div class="site-photo photo-court" role="img" aria-label="Video wall at the end of a large gymnasium"></div></div>
    <footer class="page-footer"><span class="bullet"></span>Address Goes Here<span class="sep">|</span><span class="bullet"></span>www.webaddress.com<span class="page-number">7</span></footer>
  </section>

  <section class="brochure-page">
    <header class="page-head"><div class="wordmark"><span class="wordmark-name">VELTO</span><span class="wordmark-dot"></span></div></header>
    <h2 class="site-title">St Linden Primary School</h2>
    <ul class="spec-box wide">
      <li>2x P10 800 x 640mm</li>
      <li>Framing</li>
      <li>$15,168.00</li>
      <li class="note">&#9675; Option was 2x P5 800x640<br>to enable photos for be<br>displayed $17,456.00</li>
    </ul>
    <div class="page-media"><div class="site-photo photo-street" role="img" aria-label="School entrance sign with two small screens beside a car park"></div></div>
    <footer class="page-footer"><span class="bullet"></span>Address Goes Here<span class="sep">|</span><span class="bullet"></span>www.webaddress.com<span class="page-number">8</span></footer>
  </section>

</main>
</body>
</html>
```